Visitenkarten für Elektro- und Informationstechnik-Betrieb
Zielgruppe
Wir sind ein Elektro- und Informationstechnik-Betrieb.
Unsere Fachgebiete sind Photovoltaikanlagen, Stromspeicher, Smart-Home und Ladestationrn
Aufgabenstellung
Design in der Farben des Logos und ein dunkler Hintergrund.

```html
<!DOCTYPE html>
<html lang="de">
<head>
<meta charset="utf-8">
<title>Visitenkarten – Elektro- und Informationstechnik Velten</title>
<link rel="stylesheet" href="https://fonts.googleapis.com/css2?family=Exo+2:wght@300;400;700&display=swap">
<style>
  :root{
    --page:#e8e9ec;
    --navy-top:#27353f;
    --navy-bottom:#111c24;
    --steel:#6690ad;
    --copper:#c97b4e;
    --paper:#ffffff;
    --paper-shade:#f3f5f8;
    --text-blue:#5b87a4;
  }
  *{box-sizing:border-box;margin:0;padding:0}
  html,body{width:1200px;height:1200px;overflow:hidden}
  body{
    background:var(--page);
    font-family:"Exo 2",sans-serif;
    display:flex;flex-direction:column;align-items:center;justify-content:center;gap:60px;
  }
  .card{
    position:relative;width:700px;height:453px;overflow:hidden;
    box-shadow:0 18px 40px rgba(0,0,0,.18);
  }
  .card--front{background:linear-gradient(160deg,var(--navy-top),var(--navy-bottom))}
  .card--back{background:linear-gradient(160deg,var(--paper),var(--paper-shade))}
  .band{position:absolute;height:16px}
  .band--top-copper{top:0;left:0;width:38%;background:var(--copper)}
  .band--top-steel{top:0;left:39.5%;right:0;background:var(--steel)}
  .band--bottom-steel{bottom:0;left:0;width:69%;background:var(--steel)}
  .band--bottom-copper{bottom:0;left:70.5%;right:0;background:var(--copper)}

  .brand{display:flex;align-items:center;gap:18px;color:var(--copper);font-weight:700;letter-spacing:.08em}
  .brand__square{background:var(--copper)}
  .card--front .brand{position:absolute;left:50%;top:50%;transform:translate(-50%,-50%);font-size:104px}
  .card--front .brand__square{width:46px;height:46px}
  .card--back .brand{position:absolute;left:52px;top:78px;font-size:46px}
  .card--back .brand__square{width:22px;height:22px}

  .person{position:absolute;left:90px;top:190px;color:var(--text-blue)}
  .person__name{font-size:26px;font-weight:700}
  .person__role{font-size:20px;font-weight:300;margin-top:2px}

  .contact{position:absolute;left:375px;top:120px;color:var(--text-blue);font-size:17px;line-height:1.35;font-weight:400}
  .contact__row{display:flex;gap:14px;align-items:flex-start}
  .contact__row + .contact__row{margin-top:6px}
  .contact__group{margin-top:22px}
  .contact__icon{width:18px;height:18px;flex:none;margin-top:2px;fill:none;stroke:var(--text-blue);stroke-width:1.6}
  .contact__icon--solid{fill:var(--text-blue);stroke:none}
</style>
</head>
<body>
  <section class="card card--front" aria-label="Vorderseite">
    <div class="band band--top-copper"></div>
    <div class="band band--top-steel"></div>
    <div class="brand"><span class="brand__square"></span>VELTEN</div>
    <div class="band band--bottom-steel"></div>
    <div class="band band--bottom-copper"></div>
  </section>

  <section class="card card--back" aria-label="Rückseite">
    <div class="band band--top-copper"></div>
    <div class="band band--top-steel"></div>
    <div class="brand"><span class="brand__square"></span>VELTEN</div>
    <div class="person">
      <p class="person__name">Jonas Velten</p>
      <p class="person__role">Geschäftsführer</p>
    </div>
    <div class="contact">
      <div class="contact__row">
        <svg class="contact__icon contact__icon--solid" viewBox="0 0 18 18"><path d="M9 2 1 9h2.5v7h4v-5h3v5h4V9H17z"/></svg>
        <p>Elektro- und<br>Informationstechnik Velten<br>Am Lindenhang 7<br>54311 Trierweiler</p>
      </div>
      <div class="contact__group">
        <div class="contact__row">
          <svg class="contact__icon" viewBox="0 0 18 18"><path d="M4 2l3 3-2 2c1 2 3 4 5 5l2-2 3 3-2 3C7 15 3 11 2 4z"/></svg>
          <p>+49 160 48213597</p>
        </div>
        <div class="contact__row">
          <svg class="contact__icon" viewBox="0 0 18 18"><rect x="1.5" y="4" width="15" height="10"/><path d="M1.5 4 9 10l7.5-6"/></svg>
          <p>kontakt@velten-elektro.de</p>
        </div>
        <div class="contact__row">
          <svg class="contact__icon" viewBox="0 0 18 18"><circle cx="9" cy="9" r="7"/><path d="M2 9h14M9 2c-3 3.5-3 10.5 0 14M9 2c3 3.5 3 10.5 0 14"/></svg>
          <p>www.velten-elektro.de</p>
        </div>
      </div>
    </div>
    <div class="band band--bottom-steel"></div>
    <div class="band band--bottom-copper"></div>
  </section>
</body>
</html>
```